International Reinsurance Business Platform Needs a PowerPoint Design

We need a powerpoint design for a new company based in Bermuda. We have created a platform to facilitate the incorporation and creation of off-shore reinsurance companies, primarily offered to asset managers to generate permanent capital at a fraction of the costs typically required by such a venture. We have no preference as to the color scheme, but would like for the final design to communicate professionalism, simplicity and elegance.
We have uploaded a very rudimentary draft (far from what we want), and welcome you to recreate a single page from it (it can be a combination of two pages into one; preferably something complicated enough to showcase the potential of your idea). From there, we will pick from the better submissions (of that single page) and work from there.
Target Market(s)
High-income asset managers
Industry/Entity Type
Business
Look and feel
Each slider illustrates characteristics of the customer's brand and the style your logo design should communicate.

```html
<!DOCTYPE html>
<html lang="en">
<head>
<meta charset="utf-8">
<title>Expected New AuM</title>
<link href="https://fonts.googleapis.com/css2?family=Carlito:wght@400;700&display=swap" rel="stylesheet">
<style>
  :root {
    --gold: #edbc00;
    --gold-deep: #d3a400;
    --row-tint: #fbe7a1;
    --rule: #3e3e3e;
    --text: #4f5a62;
    --white: #ffffff;
  }
  * { margin: 0; padding: 0; box-sizing: border-box; }
  html, body { width: 1200px; height: 900px; overflow: hidden; background: var(--white); }
  body { font-family: "Carlito", "Calibri", sans-serif; position: relative; }

  .slide-header {
    position: absolute; left: 0; top: 0; width: 1200px; height: 102px;
    background: var(--gold);
    border-bottom: 7px solid var(--rule);
  }
  .slide-title {
    position: absolute; left: 40px; top: 22px;
    font-size: 38px; font-weight: 700; color: var(--white); letter-spacing: 0.5px;
  }
  .brand-name {
    position: absolute; right: 34px; top: 18px;
    font-size: 62px; font-weight: 400; color: var(--white); letter-spacing: 1px; line-height: 1;
  }

  .feature-table {
    position: absolute; left: 63px; top: 249px; width: 1091px;
    border-collapse: collapse;
    box-shadow: 0 1px 4px rgba(0,0,0,0.18);
  }
  .feature-table th {
    background: var(--gold-deep); color: var(--white);
    font-size: 18px; font-weight: 700; text-align: left;
    height: 51px; padding: 0 0 0 29px; vertical-align: middle;
  }
  .feature-table td {
    color: var(--text); font-size: 18px; font-weight: 700;
    height: 78px; padding: 14px 0 0 29px; vertical-align: top; line-height: 1.6;
  }
  .feature-table .col-name { width: 372px; }
  .feature-table .col-name-cell { padding-right: 140px; }
  .feature-table tbody tr:nth-child(even) td { background: var(--row-tint); }
  .feature-table tbody tr:nth-child(odd) td { background: var(--white); }

  .slide-footer {
    position: absolute; left: 0; top: 810px; width: 1200px; height: 90px;
    background: var(--gold);
    border-top: 7px solid var(--rule);
  }
  .page-number {
    position: absolute; right: 48px; top: 38px;
    font-size: 24px; font-weight: 700; color: var(--white);
  }
</style>
</head>
<body>
  <header class="slide-header">
    <h1 class="slide-title">Expected New AuM</h1>
    <div class="brand-name">Harrow Capital</div>
  </header>

  <table class="feature-table">
    <thead>
      <tr>
        <th class="col-name">Powerful Features</th>
        <th>Powerful Features, Superior Quality, Unmatched Reliability and Dramatic Savings</th>
      </tr>
    </thead>
    <tbody>
      <tr>
        <td class="col-name-cell">End-to-End Integrated Solution</td>
        <td>ombines the best aspects of cloud-based hosted and on-premise systems.</td>
      </tr>
      <tr>
        <td class="col-name-cell">End-to-End Integrated Solution</td>
        <td>ombines the best aspects of cloud-based hosted and on-premise systems.</td>
      </tr>
      <tr>
        <td class="col-name-cell">End-to-End Integrated Solution</td>
        <td>combines the best aspects of cloud-based hosted and on-premise systems.</td>
      </tr>
      <tr>
        <td class="col-name-cell">End-to-End Integrated Solution</td>
        <td>combines the best aspects of cloud-based hosted and on-premise systems.</td>
      </tr>
    </tbody>
  </table>

  <footer class="slide-footer">
    <span class="page-number">2</span>
  </footer>
</body>
</html>
```